11 x 11 Flyer Design for Social Media - Reverse Mortgages

62 or older?

A Reverse Mortgage
could be
Your Road to Financial Freedom

* No Monthly Payments
* No Income Requirements
* No Credit Score Requirements
* No Loss of Ownership

Receive cash by lump sum, monthly installments or a line of credit!!

Call us today for a Free Consultation!!
(800) 647-2915

Harborline Financial Services, Inc.
NMLS #517830
www.harborlinefunds.example

```html
<!DOCTYPE html>
<html lang="en">
<head>
<meta charset="utf-8">
<title>Reverse Mortgage Flyer</title>
<link rel="stylesheet" href="https://fonts.googleapis.com/css2?family=Roboto:wght@700&family=Titillium+Web:ital,wght@0,400;0,700;1,700&display=swap">
<style>
  :root {
    --backdrop: #f2f2f2;
    --navy: #0f4a8c;
    --royal: #1460a8;
    --gold: #c7b22f;
    --gold-soft: #d8c86a;
    --white: #ffffff;
    --photo-sky: #a9d3f2;
    --photo-warm: #e3c796;
  }
  html, body {
    margin: 0;
    width: 1200px;
    height: 1170px;
    overflow: hidden;
    background: var(--backdrop);
  }
  .flyer {
    position: absolute;
    left: 50px;
    top: 35px;
    width: 1100px;
    height: 1100px;
    box-shadow: 0 6px 20px rgba(0,0,0,0.25);
  }
  .flyer svg { display: block; }
  .headline { font-family: "Roboto", Arial, sans-serif; font-weight: 700; }
  .headline-banner { fill: var(--royal); font-size: 37px; }
  .headline-gold { fill: var(--gold); font-size: 37px; }
  .headline-main { fill: var(--white); font-size: 49px; }
  .benefit { font-family: "Titillium Web", Arial, sans-serif; font-size: 30px; }
  .benefit-white { fill: var(--white); }
  .benefit-gold { fill: var(--gold); }
  .benefit .no { font-weight: 700; }
  .payout { font-family: "Titillium Web", Arial, sans-serif; font-style: italic; font-weight: 700; font-size: 24px; fill: var(--white); }
  .legal { font-family: "Titillium Web", Arial, sans-serif; font-size: 15px; fill: var(--gold-soft); }
  .cta { font-family: "Titillium Web", Arial, sans-serif; font-weight: 700; font-size: 27px; fill: var(--white); }
  .phone-number { font-family: "Roboto", Arial, sans-serif; font-weight: 700; font-size: 36px; fill: var(--royal); }
  .web { font-family: "Titillium Web", Arial, sans-serif; font-size: 29px; fill: var(--white); }
  .web .domain { font-weight: 700; }
  .brand-name { font-family: "Titillium Web", Arial, sans-serif; font-weight: 700; font-size: 27px; fill: var(--royal); }
  .tick { fill: none; stroke: var(--white); stroke-width: 2.2; }
</style>
</head>
<body>
<div class="flyer">
<svg width="1100" height="1100" viewBox="0 0 1100 1100" xmlns="http://www.w3.org/2000/svg">
  <defs>
    <linearGradient id="photoTone" x1="0" y1="0" x2="0.6" y2="1">
      <stop offset="0" stop-color="var(--photo-sky)"/>
      <stop offset="0.45" stop-color="#dfe9f0"/>
      <stop offset="1" stop-color="var(--photo-warm)"/>
    </linearGradient>
    <radialGradient id="panelGlow" cx="0.55" cy="0.4" r="0.7">
      <stop offset="0" stop-color="var(--royal)"/>
      <stop offset="1" stop-color="var(--navy)"/>
    </radialGradient>
  </defs>

  <!-- photo area -->
  <rect class="photo" x="0" y="0" width="760" height="1100" fill="url(#photoTone)" role="img" aria-label="Photo of a smiling senior couple embracing outdoors under a blue sky"/>

  <!-- blue panel with curved gold and white edge -->
  <path d="M262 0 C520 210 655 600 660 1100 L1100 1100 L1100 0 Z" fill="var(--white)"/>
  <path d="M282 0 C540 210 680 600 690 1100 L1100 1100 L1100 0 Z" fill="var(--gold)"/>
  <path d="M322 0 C570 220 700 600 720 1100 L1100 1100 L1100 0 Z" fill="url(#panelGlow)"/>

  <!-- headline -->
  <path d="M542 41 L1100 41 L1100 91 L542 91 L554 66 Z" fill="var(--white)"/>
  <text class="headline headline-banner" x="1056" y="81" text-anchor="end">A REVERSE MORTGAGE</text>
  <text class="headline headline-gold" x="1056" y="140" text-anchor="end">COULD BE</text>
  <text class="headline headline-main" x="1056" y="201" text-anchor="end">YOUR ROAD TO</text>
  <text class="headline headline-main" x="1056" y="251" text-anchor="end">FINANCIAL FREEDOM</text>

  <!-- benefits -->
  <g class="benefits">
    <text class="benefit benefit-white" x="1020" y="334" text-anchor="end"><tspan class="no">NO</tspan> Monthly Payments</text>
    <text class="benefit benefit-gold" x="1020" y="387" text-anchor="end"><tspan class="no">NO</tspan> Income Requirements</text>
    <text class="benefit benefit-white" x="1020" y="442" text-anchor="end"><tspan class="no">NO</tspan> Credit Score Requirements</text>
    <text class="benefit benefit-gold" x="1020" y="496" text-anchor="end"><tspan class="no">NO</tspan> Loss of Ownership</text>
    <g stroke="var(--gold-soft)" stroke-width="1.2" stroke-dasharray="2 3">
      <line x1="665" y1="352" x2="1058" y2="352"/>
      <line x1="632" y1="404" x2="1058" y2="404"/>
      <line x1="632" y1="456" x2="1058" y2="456"/>
    </g>
    <g class="tick">
      <circle cx="1044" cy="327" r="11"/><path d="M1038 326 L1043 332 L1056 317"/>
      <circle cx="1044" cy="380" r="11"/><path d="M1038 379 L1043 385 L1056 370"/>
      <circle cx="1044" cy="434" r="11"/><path d="M1038 433 L1043 439 L1056 424"/>
      <circle cx="1044" cy="489" r="11"/><path d="M1038 488 L1043 494 L1056 479"/>
    </g>
  </g>

  <!-- payout options -->
  <text class="payout" x="874" y="606" text-anchor="middle">RECEIVE CASH BY LUMP SUM,</text>
  <text class="payout" x="874" y="641" text-anchor="middle">MONTHLY INSTALLMENTS OR A</text>
  <text class="payout" x="874" y="676" text-anchor="middle">LINE OF CREDIT!!</text>
  <text class="legal" x="877" y="714" text-anchor="middle">Harborline Financial Services, Inc.</text>
  <text class="legal" x="877" y="735" text-anchor="middle">NMLS #517830</text>

  <!-- bottom right brand area -->
  <path d="M530 1100 C690 880 900 780 1100 770 L1100 1100 Z" fill="var(--gold)"/>
  <path d="M560 1100 C720 900 910 805 1100 797 L1100 1100 Z" fill="var(--white)"/>
  <circle cx="722" cy="986" r="15" fill="var(--gold)"/>
  <text class="brand-name" x="750" y="978">Harborline Financial</text>
  <text class="brand-name" x="750" y="1012">Services, Inc.</text>

  <!-- bottom left call to action -->
  <path d="M0 880 C260 858 500 900 725 1100 L0 1100 Z" fill="var(--white)"/>
  <path d="M0 898 C260 876 480 918 700 1100 L0 1100 Z" fill="var(--gold)"/>
  <text class="cta" x="30" y="943">CALL US TODAY FOR</text>
  <text class="cta" x="30" y="977">A FREE CONSULTATION!!</text>
  <path d="M0 995 L438 995 L432 1020 L438 1045 L0 1045 Z" fill="var(--white)"/>
  <g class="phone-icon" fill="var(--royal)">
    <rect x="40" y="1000" width="20" height="36" rx="3"/>
    <rect x="44" y="1005" width="12" height="24" fill="var(--white)"/>
    <path d="M30 1014 L40 1010 L40 1032 L30 1028 Z"/>
  </g>
  <text class="phone-number" x="83" y="1032">(800) 647-2915</text>
  <text class="web" x="30" y="1082">www.<tspan class="domain">harborlinefunds</tspan>.example</text>
</svg>
</div>
</body>
</html>
```